KOR Methodology infographic that shows flow of the process outlined on our web site

We are looking for a graphical representation of the methodology that is described on this web page: https://www.kor-example.com/about-kor/methodology/ We would like someone to be able to quickly understand our methodology and the key points outlined on the web page - the graphic should be able to do that.

Target Market(s)

Enterprise Companies with 1000+ employees

Industry/Entity Type

Information Technology

Font styles to use
Sans Serif

Colors
3277b5
abd036
faa54b

Requirements
Must have
• Must convey the method/process with enough detail to understand what the process is.
Nice to have
• Arrows or something showing flow would be great
Should not have
• Should not be "cartoony"

```html
<!DOCTYPE html>
<html lang="en">
<head>
<meta charset="utf-8">
<title>Methodology Process</title>
<link rel="stylesheet" href="https://fonts.googleapis.com/css2?family=Arimo:wght@400&display=swap">
<style>
  :root {
    --brand-blue: #3277b5;
    --brand-green: #abd036;
    --brand-orange: #faa54b;
    --frame-grey: #c8c8c8;
    --disc-edge: #b9bcc0;
    --page: #ffffff;
  }
  html, body {
    margin: 0;
    padding: 0;
    overflow: hidden;
    background: var(--page);
  }
  .methodology {
    position: relative;
    width: 1200px;
    height: 900px;
    box-sizing: border-box;
    border: 1px solid var(--frame-grey);
    background: var(--page);
    overflow: hidden;
    font-family: "Arimo", Arial, sans-serif;
  }
  .methodology__flow {
    position: absolute;
    inset: 0;
  }
  .step-label {
    position: absolute;
    margin: 0;
    font-size: 42px;
    font-weight: 400;
    line-height: 1;
    color: var(--brand-blue);
    white-space: nowrap;
    transform: translateX(-50%);
  }
  .step-label--consultation { left: 278px; top: 122px; }
  .step-label--development { left: 728px; top: 122px; }
  .step-label--assessment { left: 506px; top: 747px; }
  .step-label--implementation { left: 968px; top: 747px; }
</style>
</head>
<body>
<main class="methodology">
  <svg class="methodology__flow" width="1200" height="900" viewBox="0 0 1200 900" aria-hidden="true">
    <defs>
      <linearGradient id="disc-fill" x1="0" y1="0" x2="1" y2="1">
        <stop offset="0" stop-color="#e6e7e9"/>
        <stop offset="0.55" stop-color="#f6f6f7"/>
        <stop offset="1" stop-color="#ffffff"/>
      </linearGradient>
    </defs>

    <path class="flow-ribbon" d="M160 470 A117 117 0 0 0 394 470 A112 112 0 0 1 618 470 A118 118 0 0 0 854 470 A113 113 0 0 1 1080 470"
          fill="none" stroke="var(--brand-orange)" stroke-width="32"/>
    <rect x="1062" y="468" width="40" height="4" fill="var(--page)"/>

    <polygon class="flow-arrow" points="142,441 180,441 161,465" fill="var(--brand-blue)"/>
    <polygon class="flow-arrow" points="1063,478 1101,478 1082,502" fill="var(--brand-blue)"/>

    <g class="connector" stroke="var(--brand-green)" stroke-width="5" fill="var(--brand-green)">
      <line x1="277" y1="205" x2="277" y2="358"/>
      <circle cx="277" cy="205" r="10" stroke="none"/>
      <circle cx="277" cy="358" r="10" stroke="none"/>

      <line x1="506" y1="575" x2="506" y2="730"/>
      <circle cx="506" cy="575" r="10" stroke="none"/>
      <circle cx="506" cy="730" r="10" stroke="none"/>

      <line x1="737" y1="205" x2="737" y2="358"/>
      <circle cx="737" cy="205" r="10" stroke="none"/>
      <circle cx="737" cy="358" r="10" stroke="none"/>

      <line x1="965" y1="578" x2="965" y2="735"/>
      <circle cx="965" cy="578" r="10" stroke="none"/>
      <circle cx="965" cy="735" r="10" stroke="none"/>
    </g>

    <g class="step-disc" fill="url(#disc-fill)" stroke="var(--disc-edge)" stroke-width="1.5">
      <circle cx="277" cy="465" r="95"/>
      <circle cx="506" cy="468" r="95"/>
      <circle cx="736" cy="468" r="95"/>
      <circle cx="966" cy="470" r="95"/>
    </g>

    <g class="icon icon--headset" fill="none" stroke="var(--brand-blue)" stroke-linecap="round">
      <path d="M240 470 V455 A38 38 0 0 1 316 455 V470" stroke-width="8"/>
      <rect x="230" y="455" width="20" height="34" rx="8" fill="var(--brand-blue)" stroke="none"/>
      <rect x="306" y="455" width="20" height="34" rx="8" fill="var(--brand-blue)" stroke="none"/>
      <path d="M316 489 Q316 512 285 512" stroke-width="5"/>
      <circle cx="280" cy="512" r="7" fill="var(--brand-blue)" stroke="none"/>
    </g>

    <g class="icon icon--clipboard">
      <rect x="462" y="418" width="80" height="98" rx="5" fill="var(--brand-blue)"/>
      <rect x="470" y="428" width="64" height="80" fill="#ffffff"/>
      <rect x="488" y="410" width="28" height="16" rx="4" fill="var(--brand-blue)"/>
      <g stroke="var(--brand-blue)" stroke-width="4" stroke-linecap="round" fill="none">
        <path d="M476 442 l4 4 l7 -7"/><line x1="494" y1="443" x2="526" y2="443"/>
        <path d="M476 456 l4 4 l7 -7"/><line x1="494" y1="457" x2="526" y2="457"/>
        <path d="M476 470 l4 4 l7 -7"/><line x1="494" y1="471" x2="520" y2="471"/>
        <path d="M476 484 l4 4 l7 -7"/><line x1="494" y1="485" x2="512" y2="485"/>
      </g>
      <circle cx="540" cy="507" r="25" fill="#ffffff"/>
      <circle cx="540" cy="507" r="21" fill="var(--brand-blue)"/>
      <path d="M530 507 l7 7 l13 -14" stroke="#ffffff" stroke-width="5" fill="none" stroke-linecap="round" stroke-linejoin="round"/>
    </g>

    <g class="icon icon--code">
      <rect x="687" y="412" width="102" height="103" rx="4" fill="var(--brand-blue)"/>
      <rect x="718" y="419" width="62" height="7" fill="#ffffff"/>
      <circle cx="697" cy="423" r="3" fill="#ffffff"/>
      <circle cx="705" cy="423" r="3" fill="#ffffff"/>
      <circle cx="713" cy="423" r="3" fill="#ffffff"/>
      <g stroke="#ffffff" stroke-width="5" fill="none" stroke-linecap="round" stroke-linejoin="round">
        <polyline points="722,460 710,472 722,484"/>
        <polyline points="752,460 764,472 752,484"/>
        <line x1="742" y1="455" x2="732" y2="489"/>
      </g>
    </g>

    <g class="icon icon--gears" fill="var(--brand-blue)">
      <g transform="translate(936 440)">
        <circle r="22"/>
        <rect x="-6" y="-32" width="12" height="14"/>
        <rect x="-6" y="-32" width="12" height="14" transform="rotate(60)"/>
        <rect x="-6" y="-32" width="12" height="14" transform="rotate(120)"/>
        <rect x="-6" y="-32" width="12" height="14" transform="rotate(180)"/>
        <rect x="-6" y="-32" width="12" height="14" transform="rotate(240)"/>
        <rect x="-6" y="-32" width="12" height="14" transform="rotate(300)"/>
        <path d="M-10 -10 L6 6 M6 -4 V6 H-4" stroke="#ffffff" stroke-width="5" fill="none" stroke-linecap="round" stroke-linejoin="round"/>
      </g>
      <g transform="translate(990 486)">
        <circle r="32"/>
        <rect x="-8" y="-44" width="16" height="16"/>
        <rect x="-8" y="-44" width="16" height="16" transform="rotate(45)"/>
        <rect x="-8" y="-44" width="16" height="16" transform="rotate(90)"/>
        <rect x="-8" y="-44" width="16" height="16" transform="rotate(135)"/>
        <rect x="-8" y="-44" width="16" height="16" transform="rotate(180)"/>
        <rect x="-8" y="-44" width="16" height="16" transform="rotate(225)"/>
        <rect x="-8" y="-44" width="16" height="16" transform="rotate(270)"/>
        <rect x="-8" y="-44" width="16" height="16" transform="rotate(315)"/>
        <path d="M14 14 L-10 -10 M-10 4 V-10 H4" stroke="#ffffff" stroke-width="7" fill="none" stroke-linecap="round" stroke-linejoin="round"/>
      </g>
    </g>
  </svg>

  <h2 class="step-label step-label--consultation">Initial Consultation</h2>
  <h2 class="step-label step-label--development">Solution Development</h2>
  <h2 class="step-label step-label--assessment">Assessment</h2>
  <h2 class="step-label step-label--implementation">Implementation</h2>
</main>
</body>
</html>
```